Upscale business cards needed for family office

We would like professional business cards created for employees of our family office. Relatively simple and straightforward, but also with a unique element to set them apart. Probably stick with neutral and simple colors that mesh well with the colors in the logo. We need space for the traditional elements, including name, title, address, email/phone number.

Industry/Entity Type

Business

Contact Information for Business Card

Space for name, title, phone number, email, address

```html
<!DOCTYPE html>
<html lang="en">
<head>
<meta charset="utf-8">
<title>Marlow Ridge Business Card</title>
<link rel="stylesheet" href="https://fonts.googleapis.com/css2?family=Arimo:wght@400;700&display=swap">
<style>
  :root {
    --page-bg: #e9e7e3;
    --card-bg: #f3f4f4;
    --card-edge: #c9cccd;
    --frame-line: #55595c;
    --ink: #2c2e30;
    --accent: #1e5b7c;
    --brand-ink: #3f4346;
  }
  * { box-sizing: border-box; margin: 0; padding: 0; }
  html, body {
    width: 1200px;
    height: 969px;
    overflow: hidden;
    background: var(--page-bg);
    font-family: "Arimo", Arial, sans-serif;
  }
  .card {
    position: absolute;
    left: 120px;
    top: 212px;
    width: 960px;
    height: 545px;
    background: var(--card-bg);
    border: 1px solid var(--card-edge);
    box-shadow: 0 10px 30px rgba(0,0,0,0.12);
  }
  .card-frame {
    position: absolute;
    left: 44px;
    top: 26px;
    width: 881px;
    height: 471px;
    border: 3px solid var(--frame-line);
    display: flex;
  }
  .brand-panel {
    width: 441px;
    height: 100%;
    border-right: 3px solid var(--frame-line);
    display: flex;
    flex-direction: column;
    align-items: center;
    justify-content: center;
    gap: 28px;
  }
  .brand-square {
    width: 64px;
    height: 64px;
    background: var(--accent);
  }
  .brand-name {
    font-family: "Arimo", Arial, sans-serif;
    font-weight: 700;
    font-size: 40px;
    line-height: 1;
    color: var(--brand-ink);
    letter-spacing: 2px;
    text-transform: uppercase;
  }
  .contact-panel {
    flex: 1;
    padding: 86px 0 0 88px;
    color: var(--ink);
  }
  .person-name {
    font-size: 31px;
    font-weight: 700;
    color: var(--accent);
    letter-spacing: 0.5px;
    text-transform: uppercase;
  }
  .person-title {
    font-size: 24px;
    color: var(--accent);
    margin-top: 8px;
    text-transform: uppercase;
    letter-spacing: 0.5px;
  }
  .address {
    font-size: 24px;
    line-height: 34px;
    margin-top: 44px;
    font-style: normal;
  }
  .contact-list {
    list-style: none;
    font-size: 23px;
    line-height: 36px;
    margin-top: 18px;
  }
  .contact-label {
    font-weight: 700;
    color: var(--accent);
    margin-right: 4px;
  }
</style>
</head>
<body>
  <div class="card">
    <div class="card-frame">
      <div class="brand-panel">
        <span class="brand-square"></span>
        <span class="brand-name">Marlow Ridge</span>
      </div>
      <div class="contact-panel">
        <h1 class="person-name">Daniel Ashford</h1>
        <p class="person-title">President</p>
        <address class="address">2719 Linden Court<br>Cedar Grove, NY 10542</address>
        <ul class="contact-list">
          <li><span class="contact-label">P :</span> 555 0148 2731</li>
          <li><span class="contact-label">E :</span> daniel@example.com</li>
          <li><span class="contact-label">W :</span> www.example.com</li>
        </ul>
      </div>
    </div>
  </div>
</body>
</html>
```